Business card design - landscaping industry

Hello! We are very creative when it comes to landscape design but when it comes to designing business cards - not so much. We could use some help to come up with a design which is professional but fun. We are based in Grand Rapids, MI and work with high end properties for new landscape design and install. We are looking to have a template made for business card for a couple of us on staff.

You can get the flavor of our color scheme from our attached logo. We probably would want to highlight the green but also include some of the blue maybe.

Target Market(s)

We work with residential homeowners here in West Michigan. Very nice people by and large.

Industry/Entity Type

Landscaping

Contact Information for Business Card

The card should be standard size with round edges maybe?

Font styles to use
Serif
Sans Serif
Decorative

Requirements
Must have
• Must haves:
• 1. Address: 4817 Birchwell Meadow Lane SE, Grand Rapids, Michigan 49582
• 2. Phone: 616.555.0187
• 3. Email: company@larkhollowyard.com
• 4. URL: www.larkhollowyard.com
• 5. Names/Titles: (1) Dennis Harlow, President (2) Tomas Belvin, Director of Field Services
Nice to have
• On the back side of the card, we are thinking it would make sense to have a short listing of services offered...
• Landscape design & installation, Professional lawn maintenance, Spring & fall leaf cleanup, Irrigation system installation & maintenance, Snowplowing, Fertilizer & weed control, Tree maintenance and removal, Landscape bed maintenance
Should not have
• Our hope is that the design won't be too ostentatious. We are looking for professional and attractive.

```html
<!DOCTYPE html>
<html lang="en">
<head>
<meta charset="utf-8">
<title>Lark Hollow Landscaping — Stationery</title>
<link href="https://fonts.googleapis.com/css2?family=Cinzel:wght@500&family=Questrial&family=Oswald:wght@400&display=swap" rel="stylesheet">
<style>
  :root{
    --bg:#e2e2e2;
    --ink:#1c1c1c;
    --paper:#f4f4f4;
    --paper-edge:#ffffff;
    --silver:#d6d6d6;
    --blue:#2d8fd5;
    --green:#3cb35a;
    --body:#555;
    --muted:#bdbdbd;
  }
  *{margin:0;padding:0;box-sizing:border-box}
  html,body{width:1200px;height:899px;overflow:hidden;background:var(--bg)}
  .stage{position:relative;width:1200px;height:899px;font-family:"Questrial",sans-serif}
  .piece{position:absolute}
  .brand{font-family:"Cinzel",serif;font-weight:500;color:var(--silver);letter-spacing:.18em;white-space:nowrap}

  /* letterhead */
  .letterhead{left:153px;top:80px;width:377px;height:532px;background:var(--paper)}
  .letterhead .band{height:72px;background:var(--ink);position:relative}
  .letterhead .brand{position:absolute;left:33px;top:37px;font-size:13px}
  .letterhead .rule{position:absolute;left:255px;top:30px;width:1px;height:34px;background:#555}
  .contact{list-style:none;color:#e8e8e8;font-size:5.6px;line-height:7.6px}
  .contact li{display:flex;align-items:center;gap:3px}
  .contact svg{width:5px;height:5px;flex:none}
  .letterhead .contact{position:absolute;left:263px;top:32px}
  .letter{position:absolute;left:33px;top:148px;width:313px;color:var(--body)}
  .letter .greeting{font-size:9.5px;color:#444;margin-bottom:17px}
  .letter p{font-size:5.3px;line-height:8.1px;margin-bottom:8px;text-align:justify}
  .letter .closing{margin-top:16px}
  .signature{display:block;width:67px;height:28px;margin-top:6px;background:linear-gradient(90deg,#cfe3f4,#e6eff7)}
  .footer-address{position:absolute;left:0;right:0;display:flex;justify-content:center;align-items:center;gap:3px;font-size:5.6px;color:#555}
  .footer-address svg{width:5px;height:6px}
  .letterhead .footer-address{top:586px;top:auto;bottom:22px}

  /* folder */
  .folder{left:564px;top:48px;width:445px;height:565px;background:var(--ink)}
  .folder .spine{position:absolute;top:0;bottom:0;width:1px;background:#3a3a3a}
  .folder .brand{position:absolute;left:0;right:0;top:316px;text-align:center;font-size:30px;letter-spacing:.14em}

  /* business cards */
  .card{width:157px;height:90px;background:var(--ink);left:66px}
  .card-front{top:656px}
  .card-front .brand{position:absolute;left:0;right:0;top:27px;text-align:center;font-size:9px}
  .card-front .services-title{position:absolute;left:0;right:0;top:52px;text-align:center;font-family:"Cinzel",serif;font-size:4px;color:var(--green);letter-spacing:.05em}
  .card-front .services{position:absolute;left:10px;right:10px;top:61px;text-align:center;color:#dcdcdc;font-size:3.6px;line-height:4.8px}
  .card-back{top:762px}
  .card-back .person{position:absolute;left:14px;top:37px;text-align:center}
  .card-back .name{font-family:"Oswald",sans-serif;font-size:7.5px;color:var(--blue);letter-spacing:.02em}
  .card-back .title{font-size:3.6px;color:var(--blue);letter-spacing:.03em}
  .card-back .rule{position:absolute;left:88px;top:35px;width:1px;height:22px;background:#666}
  .card-back .contact{position:absolute;left:92px;top:35px;font-size:3.6px;line-height:5px}
  .card-back .contact svg{width:3.5px;height:3.5px}
  .card-back .footer-address{bottom:9px;font-size:3.6px;color:#e0e0e0}
  .card-back .footer-address svg{width:3.5px;height:4px}

  /* envelopes */
  .envelope{background:var(--paper)}
  .envelope-flat{left:242px;top:655px;width:436px;height:199px}
  .envelope-flat .band{height:72px;background:var(--ink);position:relative}
  .envelope-flat .brand{position:absolute;left:26px;top:30px;font-size:10px}
  .envelope-flat .footer-address{bottom:20px}
  .envelope-flap{left:700px;top:654px;width:435px;height:198px}
  .envelope-flap svg.flap{position:absolute;left:0;top:0;width:435px;height:62px}
  .envelope-flap .brand{position:absolute;left:0;right:0;top:25px;text-align:center;font-size:8px}
</style>
</head>
<body>
<main class="stage">

  <!-- Letterhead -->
  <article class="piece letterhead">
    <header class="band">
      <span class="brand">LARK HOLLOW</span>
      <span class="rule"></span>
      <ul class="contact">
        <li><svg viewBox="0 0 10 10"><path fill="var(--blue)" d="M2 0.5l2 2-1 1.3c.6 1.3 1.6 2.3 2.9 2.9L7.2 5.7l2.3 2-1.2 1.8C4.5 9.4.6 5.5.5 1.7z"/></svg>616.555.0187</li>
        <li><svg viewBox="0 0 10 10"><rect x="0.5" y="2" width="9" height="6" fill="var(--blue)"/></svg>company@larkhollowyard.com</li>
        <li><svg viewBox="0 0 10 10"><circle cx="5" cy="5" r="4.5" fill="var(--blue)"/></svg>www.larkhollowyard.com</li>
      </ul>
    </header>
    <section class="letter">
      <p class="greeting">Dear Mr. Avery,</p>
      <p>Lorem ipsum dolor sit amet, consectetur adipiscing elit. Donec orci purus, luctus vitae dignissim eu, iaculis sed purus. Vivamus faucibus, ipsum nec aliquet viverra, leo mauris condimentum ligula, sit amet sagittis enim ligula quis arcu. Nam egestas tortor id nisi porttitor mattis. In tortor ante, ultricies in suscipit a, tempus non massa. Vivamus et auctor mi. Fusce vel massa nulla. Phasellus nec eros mauris, et scelerisque orci.</p>
      <p>Donec malesuada orci vitae nulla accumsan porta a id massa. Quisque accumsan iaculis magna sit amet fringilla. Maecenas consequat, magna eget tincidunt semper, odio nibh rutrum mi, id feugiat ante nisi eu risus. Vestibulum nunc orci, rhoncus a placerat in, ultricies in mi. Cras mattis varius eros, vel fringilla nisi suscipit eget. Quisque scelerisque sagittis nulla at porttitor.</p>
      <p>Sed id augue vitae urna euismod commodo aliquet a quam. Pellentesque arcu velit, cursus et malesuada ut, consequat et diam. Nullam erat sem, rhoncus id ullamcorper vitae, rhoncus et arcu. In ultricies ultricies nulla, ut rutrum nisi iaculis at. Donec eu magna a metus ornare faucibus. Fusce aliquet faucibus ultricies. Morbi semper, est id tincidunt gravida, sem arcu adipiscing lacus, ac bibendum nulla leo eu purus. Quisque nec diam sed risus consectetur a accumsan quis quis nibh. Vestibulum id purus lorem.</p>
      <p>It is a long established fact that a reader will be distracted by the readable content of a page when looking at its layout. The point of using Lorem Ipsum is that it has a more-or-less normal distribution of letters, as opposed to using 'Content here, content here', making it look like readable English. Many desktop publishing packages</p>
      <p class="closing">Sincerely,</p>
      <span class="signature" role="img" aria-label="Handwritten signature of Paul Avery in blue ink"></span>
    </section>
    <p class="footer-address"><svg viewBox="0 0 10 12"><path fill="var(--blue)" d="M5 0a4.5 4.5 0 0 0-4.5 4.5C.5 8 5 12 5 12s4.5-4 4.5-7.5A4.5 4.5 0 0 0 5 0zm0 6.3a1.8 1.8 0 1 1 0-3.6 1.8 1.8 0 0 1 0 3.6z"/></svg>4817 Birchwell Meadow Lane SE, Grand Rapids, Michigan 49582</p>
  </article>

  <!-- Presentation folder -->
  <article class="piece folder">
    <span class="spine" style="left:6px"></span>
    <span class="spine" style="left:14px"></span>
    <span class="spine" style="left:23px"></span>
    <span class="brand">LARK HOLLOW</span>
  </article>

  <!-- Business card: services side -->
  <article class="piece card card-front">
    <span class="brand">LARK HOLLOW</span>
    <p class="services-title">SERVICES OFFERED</p>
    <p class="services">Landscape design &amp; installation • Professional lawn maintenance<br>Spring &amp; fall leaf cleanup • Irrigation system installation &amp; maintenance<br>Snowplowing • Fertilizer &amp; weed control • Tree maintenance &amp; removal<br>Landscape bed maintenance</p>
  </article>

  <!-- Business card: contact side -->
  <article class="piece card card-back">
    <div class="person">
      <p class="name">TOMAS BELVIN</p>
      <p class="title">DIRECTOR OF FIELD SERVICES</p>
    </div>
    <span class="rule"></span>
    <ul class="contact">
      <li><svg viewBox="0 0 10 10"><path fill="var(--blue)" d="M2 0.5l2 2-1 1.3c.6 1.3 1.6 2.3 2.9 2.9L7.2 5.7l2.3 2-1.2 1.8C4.5 9.4.6 5.5.5 1.7z"/></svg>616.555.0187</li>
      <li><svg viewBox="0 0 10 10"><rect x="2.5" y="0.5" width="5" height="9" rx="1" fill="var(--blue)"/></svg>616.555.0243</li>
      <li><svg viewBox="0 0 10 10"><rect x="0.5" y="2" width="9" height="6" fill="var(--blue)"/></svg>company@larkhollowyard.com</li>
      <li><svg viewBox="0 0 10 10"><circle cx="5" cy="5" r="4.5" fill="var(--blue)"/></svg>www.larkhollowyard.com</li>
    </ul>
    <p class="footer-address"><svg viewBox="0 0 10 12"><path fill="var(--blue)" d="M5 0a4.5 4.5 0 0 0-4.5 4.5C.5 8 5 12 5 12s4.5-4 4.5-7.5A4.5 4.5 0 0 0 5 0zm0 6.3a1.8 1.8 0 1 1 0-3.6 1.8 1.8 0 0 1 0 3.6z"/></svg>4817 Birchwell Meadow Lane SE, Grand Rapids, Michigan 49582</p>
  </article>

  <!-- Envelope, front -->
  <article class="piece envelope envelope-flat">
    <header class="band"><span class="brand">LARK HOLLOW</span></header>
    <p class="footer-address"><svg viewBox="0 0 10 12"><path fill="var(--blue)" d="M5 0a4.5 4.5 0 0 0-4.5 4.5C.5 8 5 12 5 12s4.5-4 4.5-7.5A4.5 4.5 0 0 0 5 0zm0 6.3a1.8 1.8 0 1 1 0-3.6 1.8 1.8 0 0 1 0 3.6z"/></svg>4817 Birchwell Meadow Lane SE, Grand Rapids, Michigan 49582</p>
  </article>

  <!-- Envelope, back with flap -->
  <article class="piece envelope envelope-flap">
    <svg class="flap" viewBox="0 0 435 62" preserveAspectRatio="none"><path fill="var(--ink)" d="M0 0H435V6C435 12 428 18 420 26L392 52C386 58 380 62 370 62H65C55 62 49 58 43 52L15 26C7 18 0 12 0 6Z"/></svg>
    <span class="brand">LARK HOLLOW</span>
  </article>

</main>
</body>
</html>
```